Design 5 colour schemes for one web page

We are looking for 5 different colour schemes for our product template to create different kinds of colour tone for our web page, it doesn't need to be restructure the layout, just need to provide different color solution.

Please refer to the attached images and take note of the following when you’re working on the design:
(1) Please precisely reproduce the layout. Cannot remove or delete any wordings, components or column shown in the images.
(2) Okay to revise icons, background color or text style as you prefer. But cannot move/delete them.
(3) Provide PSD source files with good layer management. HTML/CSS are not required.
(4) Make reasonable and professional design.

After completion, please send back:
(1) 5 images with 5 different colour schemes.
(2) Related PSD files.

Industry/Entity Type

Management

Number of Pages Required

1 page

Font styles to use
Serif
Sans Serif

Requirements
Must have
• (1) 5 images for the colour schemes.
• (2) 5 PSD source files with good layer management.
Nice to have
• (1) Explanation about your design of the colour schemes.
Should not have
• (1) HTML/CSS code are not required.

```html
<!DOCTYPE html>
<html lang="en">
<head>
<meta charset="utf-8">
<title>Sports Events</title>
<link href="https://fonts.googleapis.com/css2?family=Open+Sans:wght@400;600;700;800&display=swap" rel="stylesheet">
<style>
:root{
  --primary:#6a4fb3; --primary-dark:#55399c; --primary-light:#8468c9; --signout:#5e43a6;
  --title:#5a3fa6; --accent:#f6c343; --accent-text:#7a5a0c;
  --colhead:#2f9ccc; --colhead-line:#5bb6de;
  --league:#e2486f; --side:#29233f; --side-line:#3a3358; --side-tab:#332b4f;
  --row-a:#f1f4fb; --row-b:#e8e6f4; --row-gray:#f0f0f0; --row-warm:#f6ece0;
  --text:#333; --odd-blue:#2f9ccc; --odd-red:#c23a5c; --toolbar-a:#e9e7ef; --toolbar-b:#d7d4e0;
}
*{box-sizing:border-box;margin:0;padding:0}
html,body{width:996px;height:1200px;overflow:hidden;background:#fff}
body{font-family:"Open Sans",Arial,sans-serif;color:var(--text)}
.page{position:absolute;left:0;top:0;width:1150px;height:1386px;transform:scale(.8661);transform-origin:0 0}
.abs{position:absolute}
svg.ic{display:inline-block;vertical-align:middle}
.topbar{left:0;top:0;width:1150px;height:43px;background:var(--primary);color:#fff;font-size:12px}
.topbar .nav span{position:absolute;top:13px}
.topbar .hi{position:absolute;left:746px;top:13px}
.balance{position:absolute;left:828px;top:0;width:174px;height:43px;background:var(--primary-dark);font-weight:600;font-size:13px;line-height:43px;padding-left:18px}
.signout{position:absolute;left:1002px;top:0;width:85px;height:43px;background:var(--signout);font-weight:600;font-size:13px;line-height:43px;text-align:center}
.title{left:63px;top:62px;font-size:40px;font-weight:800;color:var(--title);letter-spacing:.5px;line-height:50px}
.tab-sports{left:476px;top:76px;width:121px;height:48px;background:var(--accent);color:var(--accent-text);font-size:14px;text-align:center;line-height:46px;border-radius:3px 3px 0 0}
.results{left:1004px;top:72px;font-size:12px;color:#999;display:flex;align-items:center;gap:6px}
.toolbar{left:0;top:124px;width:1150px;height:48px;background:linear-gradient(var(--toolbar-a),var(--toolbar-b));font-size:13px}
.tb-cell{position:absolute;top:0;height:48px;line-height:48px;border-right:1px solid #c6c2d2;color:#333}
.caret{display:inline-block;width:0;height:0;border-left:6px solid transparent;border-right:6px solid transparent;border-top:7px solid #777;vertical-align:middle;margin-left:12px}
.panel-head{height:44px;line-height:44px;color:#fff;font-size:15px;padding-left:22px;background:linear-gradient(var(--primary-light),var(--primary))}
.fav-body{height:107px;background:#eee;padding:11px 10px}
.fav-body div{border:1px dashed #bbb;height:73px;text-align:center;font-size:13px;color:#555;padding-top:16px;line-height:18px}
.tabs{display:flex;height:44px;font-size:15px}
.tabs div{flex:1;line-height:44px;text-align:center;color:#fff}
.sports-list{background:var(--side);padding:4px 6px 10px}
.sport{height:28.1px;display:flex;align-items:center;color:#fff;font-weight:700;font-size:14px;border-bottom:1px solid var(--side-line);letter-spacing:-.2px}
.sport svg{width:22px;height:20px;margin:0 10px 0 6px;flex:none}
.sport b{margin-left:auto;margin-right:4px}
.mybets-body{height:99px;background:#eee;text-align:center;font-size:13px;padding-top:18px}
.nopending{margin:9px 10px 0;height:33px;line-height:33px;background:var(--league);color:#fff}
.viewall{height:26px;line-height:26px;background:var(--accent);text-align:center;font-size:12px}
.sec-head{height:44px;background:linear-gradient(var(--primary-light),var(--primary));color:#fff;position:relative}
.sec-head .t{position:absolute;left:18px;top:10px;font-size:15px}
.sec-head .c{position:absolute;left:370px;top:13px;font-size:13px}
.sec-head .s{position:absolute;right:17px;top:13px;font-size:13px}
.col-head{height:64px;position:relative;font-size:12px}
.col-head span{position:absolute;line-height:16px}
.col-head .vl{position:absolute;top:0;width:1px;height:64px}
.col-head .hl{position:absolute;top:32px;height:1px}
.col-strong{background:var(--colhead);color:#fff}
.col-strong .vl,.col-strong .hl{background:var(--colhead-line)}
.col-light{background:#f1f4fb;color:#333}
.col-light .vl,.col-light .hl{background:#d9dcea}
.league{height:40px;background:var(--league);color:#fff;font-size:12px;position:relative}
.league .star{position:absolute;left:84px;top:13px}
.league .n{position:absolute;left:109px;top:12px}
.league .r{position:absolute;right:12px;top:10px}
.row{height:62px;position:relative;font-size:12px;border-bottom:2px solid #fff}
.row span{position:absolute;line-height:16px}
.row .div{position:absolute;top:0;width:1px;height:100%;background:#fff}
.row .bars{position:absolute;left:9px;top:28px}
.ra{background:var(--row-a)} .rb{background:var(--row-b)} .rg{background:var(--row-gray)} .rw{background:var(--row-warm)}
.ob{color:var(--odd-blue);font-size:11px}.or{color:var(--odd-red)}
.footer{left:0;top:1288px;width:1150px;height:98px;background:#ebebeb;font-size:12px;color:#444;text-align:center}
</style>
</head>
<body>
<svg width="0" height="0" style="position:absolute">
  <defs>
    <symbol id="bars" viewBox="0 0 14 12"><rect x="0" y="8" width="3" height="4"/><rect x="4" y="5" width="3" height="7"/><rect x="8" y="2" width="3" height="10"/><rect x="12" y="0" width="2" height="12"/></symbol>
    <symbol id="refresh" viewBox="0 0 20 20"><path d="M16 10a6 6 0 1 1-2-4.5" fill="none" stroke="currentColor" stroke-width="2"/><path d="M15 2v5h-5" fill="none" stroke="currentColor" stroke-width="2"/></symbol>
    <symbol id="trophy" viewBox="0 0 20 20"><path d="M5 2h10v5a5 5 0 0 1-10 0zM2 3h3v3H4a2 2 0 0 1-2-2zM18 3h-3v3h1a2 2 0 0 0 2-2zM9 12h2v3H9zM6 16h8v2H6z" fill="currentColor"/></symbol>
    <symbol id="runner" viewBox="0 0 20 20"><circle cx="13" cy="3" r="2" fill="currentColor"/><path d="M6 7l5-1 2 4 4 1M11 6l-2 6-5 3M9 12l4 3-1 4" fill="none" stroke="currentColor" stroke-width="2" stroke-linecap="round"/></symbol>
  </defs>
</svg>
<div class="page">

<div class="abs topbar">
  <div class="nav"><span style="left:84px">My Bets</span><span style="left:159px">Statement</span><span style="left:248px">Preference</span><span style="left:341px">Announcements</span></div>
  <span class="hi">Hi, stwtg036</span>
  <div class="balance">❯❯&nbsp; SD$ &nbsp;10,072.00 &nbsp;<svg class="ic" width="13" height="13" style="color:#fff"><use href="#refresh"/></svg></div>
  <div class="signout">Sign out</div>
</div>

<div class="abs title">SPORTS EVENTS</div>
<div class="abs tab-sports">SPORTS</div>
<div class="abs results"><svg width="38" height="30" viewBox="0 0 38 30"><path d="M2 22h34l-4 6H6z" fill="var(--league)"/><circle cx="19" cy="12" r="10" fill="var(--league)"/><text x="19" y="16" font-size="11" fill="#fff" text-anchor="middle" font-family="Open Sans">1</text></svg>Results</div>

<div class="abs toolbar">
  <div class="tb-cell" style="left:63px;width:175px;padding-left:18px;border-left:1px solid #c6c2d2"><svg class="ic" width="22" height="22" viewBox="0 0 22 22" style="margin-right:8px"><circle cx="11" cy="11" r="10" fill="none" stroke="#555" stroke-width="2"/><path d="M5 6l4 3-1 4 3 2M14 3l-1 4 4 2" stroke="#555" stroke-width="2" fill="none"/></svg>Results (Asia)<span class="caret"></span></div>
  <div class="tb-cell" style="left:238px;width:238px;padding-left:20px">20/12/2014 &nbsp;14 : 26 PM &nbsp; GMT + 8</div>
  <div class="tb-cell" style="left:597px;width:70px;padding-left:14px;border-left:1px solid #c6c2d2"><svg class="ic" width="18" height="18" viewBox="0 0 18 18"><circle cx="9" cy="9" r="8" fill="none" stroke="#666" stroke-width="1.3"/><path d="M9 5v8M5 9h8" stroke="#666" stroke-width="1.3"/></svg><span class="caret"></span></div>
  <div class="tb-cell" style="left:667px;width:70px;padding-left:14px"><svg class="ic" width="18" height="18" viewBox="0 0 20 20"><path d="M10 1l2.6 6 6.4.5-4.9 4.2 1.5 6.3L10 14.6 4.4 18l1.5-6.3L1 7.5 7.4 7z" fill="#444"/></svg><span class="caret"></span></div>
  <div class="tb-cell" style="left:737px;width:70px;padding-left:14px"><svg class="ic" width="20" height="16" viewBox="0 0 20 16"><rect x="0" y="1" width="20" height="14" fill="#444"/><path d="M3 5h14M3 8h14M3 11h14" stroke="#ddd"/></svg><span class="caret"></span></div>
  <div class="tb-cell" style="left:807px;width:70px;padding-left:14px">My<span class="caret"></span></div>
  <div class="tb-cell" style="left:877px;width:70px;padding-left:14px"><svg class="ic" width="20" height="16" viewBox="0 0 20 16"><path d="M1 5h4l5-4v14l-5-4H1z" fill="#444"/><path d="M13 5a4 4 0 0 1 0 6M15 3a7 7 0 0 1 0 10" stroke="#444" fill="none" stroke-width="1.4"/></svg><span class="caret"></span></div>
  <div class="tb-cell" style="left:947px;width:70px;padding-left:14px"><svg class="ic" width="20" height="18" viewBox="0 0 20 18"><rect x="1" y="5" width="15" height="11" fill="none" stroke="#444" stroke-width="2"/><path d="M6 1l3 4 5-4" stroke="#444" fill="none" stroke-width="1.5"/></svg><span class="caret"></span></div>
  <div class="tb-cell" style="left:1017px;width:70px;padding-left:14px;border-right:none">Live<span class="caret"></span></div>
</div>

<div class="abs" style="left:63px;top:190px;width:220px">
  <div class="panel-head">My Favourites</div>
  <div class="fav-body"><div>Click an event or league<br>to add it it “My Favourites”</div></div>
</div>

<div class="abs" style="left:63px;top:351px;width:220px">
  <div class="tabs"><div style="background:var(--side-tab)">Sports</div><div style="background:var(--primary)">Markets</div></div>
  <div class="sports-list">
    <div class="sport"><svg viewBox="0 0 22 20" fill="none" stroke="#fff" stroke-width="1.6"><circle cx="11" cy="10" r="8"/><path d="M11 6l3 2-1 4h-4l-1-4z" fill="#fff"/></svg>Football<b>600</b></div>
    <div class="sport"><svg viewBox="0 0 22 20" fill="none" stroke="#fff" stroke-width="1.6"><circle cx="11" cy="10" r="8"/><path d="M3 10h16M11 2v16M5 4c4 3 4 9 0 12M17 4c-4 3-4 9 0 12"/></svg>Basketball<b>600</b></div>
    <div class="sport"><svg viewBox="0 0 22 20" fill="none" stroke="#fff" stroke-width="1.6"><circle cx="11" cy="10" r="8"/><path d="M6 4c3 3 3 9 0 12M16 4c-3 3-3 9 0 12"/></svg>Baseball<b>600</b></div>
    <div class="sport"><svg viewBox="0 0 22 20" fill="none" stroke="#fff" stroke-width="1.8"><ellipse cx="14" cy="7" rx="5" ry="6" transform="rotate(40 14 7)"/><path d="M10 12l-7 7"/></svg>Tennis<b>600</b></div>
    <div class="sport"><svg viewBox="0 0 22 20" fill="none" stroke="#fff" stroke-width="1.6"><ellipse cx="11" cy="10" rx="9" ry="6"/><path d="M7 10h8M9 8v4M11 8v4M13 8v4"/></svg>American Football<b>600</b></div>
    <div class="sport"><svg viewBox="0 0 22 20" fill="none" stroke="#fff" stroke-width="1.6"><path d="M6 3l10 0-3 9h-4z"/><circle cx="11" cy="15" r="3" fill="#fff"/></svg>Badminton<b>600</b></div>
    <div class="sport"><svg viewBox="0 0 22 20" fill="#fff"><rect x="4" y="3" width="13" height="11" rx="5"/><rect x="6" y="14" width="9" height="4"/></svg>Boxing<b>600</b></div>
    <div class="sport"><svg viewBox="0 0 22 20" fill="#fff"><rect x="9" y="1" width="5" height="15" rx="1" transform="rotate(40 11 10)"/><circle cx="17" cy="16" r="2.5"/></svg>Cricket<b>600</b></div>
    <div class="sport"><svg viewBox="0 0 22 20" fill="none" stroke="#fff" stroke-width="1.6"><circle cx="5" cy="14" r="4"/><circle cx="17" cy="14" r="4"/><path d="M5 14l4-7h6l2 7M9 7l3 7"/></svg>Cycling<b>600</b></div>
    <div class="sport"><svg viewBox="0 0 22 20" fill="none" stroke="#fff" stroke-width="1.6"><circle cx="10" cy="11" r="8"/><circle cx="10" cy="11" r="4"/><circle cx="10" cy="11" r="1" fill="#fff"/><path d="M10 11l10-9"/></svg>Darts<b>600</b></div>
    <div class="sport"><svg viewBox="0 0 22 20" fill="#fff"><path d="M2 5l4 5 5-7 5 7 4-5-2 11H4z"/></svg>Entertainment<b>600</b></div>
    <div class="sport"><svg viewBox="0 0 22 20" fill="none" stroke="#fff" stroke-width="1.8"><path d="M7 18V2"/><path d="M7 2l9 4-9 4z" fill="#fff"/><path d="M3 18h10"/></svg>Golf<b>600</b></div>
    <div class="sport"><svg viewBox="0 0 22 20" fill="none" stroke="#fff" stroke-width="1.6"><circle cx="11" cy="10" r="8"/><path d="M4 7c5 2 9 2 14 0M4 13c5-2 9-2 14 0"/></svg>Handball<b>600</b></div>
    <div class="sport"><svg viewBox="0 0 22 20" fill="none" stroke="#fff" stroke-width="2"><path d="M15 2L8 16H3"/><rect x="15" y="15" width="5" height="2" fill="#fff"/></svg>Ice Hockey<b>600</b></div>
    <div class="sport"><svg viewBox="0 0 22 20" fill="#fff"><rect x="4" y="5" width="14" height="10" rx="3"/><path d="M8 5v-2M12 5v-2M16 5v-2" stroke="#fff" stroke-width="2"/></svg>Mixed Martial Arts<b>600</b></div>
    <div class="sport"><svg viewBox="0 0 22 20"><path d="M4 2v17" stroke="#fff" stroke-width="2"/><rect x="5" y="2" width="14" height="10" fill="#fff"/><path d="M5 2h3.5v2.5H5zM12 2h3.5v2.5H12zM8.5 4.5H12V7H8.5zM15.5 4.5H19V7h-3.5zM5 7h3.5v2.5H5zM12 7h3.5v2.5H12z" fill="var(--side)"/></svg>Miotor Sport<b>600</b></div>
    <div class="sport"><svg viewBox="0 0 22 20" fill="#fff"><circle cx="11" cy="4" r="2.3"/><circle cx="8.5" cy="8.5" r="2.3"/><circle cx="13.5" cy="8.5" r="2.3"/><circle cx="6" cy="13" r="2.3"/><circle cx="11" cy="13" r="2.3"/><circle cx="16" cy="13" r="2.3"/></svg>Pool/Snooker<b>600</b></div>
    <div class="sport"><svg viewBox="0 0 22 20" fill="none" stroke="#fff" stroke-width="1.6"><ellipse cx="11" cy="10" rx="9" ry="6" transform="rotate(-30 11 10)"/><path d="M7 13l8-6"/></svg>Rugby<b>600</b></div>
    <div class="sport"><svg viewBox="0 0 22 20" fill="none" stroke="#fff" stroke-width="1.6"><circle cx="11" cy="10" r="8"/><path d="M11 2c-2 4 0 8 7 10M3 9c4-1 8 1 10 8M6 4c3 2 8 2 11 1"/></svg>Volleyball<b>600</b></div>
    <div class="sport" style="border-bottom:none"><svg viewBox="0 0 22 20" fill="none" stroke="#fff" stroke-width="1.6"><path d="M11 1v18M3 5.5l16 9M3 14.5l16-9M8 2l3 2 3-2M8 18l3-2 3 2"/></svg>Winter Sports<b>600</b></div>
  </div>
</div>

<div class="abs" style="left:63px;top:985px;width:220px">
  <div class="tabs"><div style="background:var(--side-tab)">Ticket</div><div style="background:var(--primary)">Parlay <svg class="ic" width="16" height="16" viewBox="0 0 16 16"><rect x="1" y="1" width="14" height="14" fill="none" stroke="#fff" stroke-width="2"/><rect x="4" y="4" width="8" height="8" fill="#fff"/></svg></div></div>
  <div style="height:39px;background:var(--side-tab)"></div>
</div>

<div class="abs" style="left:63px;top:1077px;width:220px">
  <div class="panel-head">My Bets</div>
  <div class="mybets-body"><svg class="ic" width="13" height="13" style="color:#444"><use href="#refresh"/></svg> Refresh<div class="nopending">No Pending bets</div></div>
  <div class="viewall">View all</div>
</div>

<div class="abs" style="left:293px;top:190px;width:794px">
  <div class="sec-head"><span class="t"><svg class="ic" width="20" height="20" style="color:#fff;margin-right:4px"><use href="#runner"/></svg> Today Live</span><span class="c"><svg class="ic" width="14" height="14" style="color:#fff"><use href="#refresh"/></svg> 38</span><span class="s"><svg class="ic" width="16" height="16" style="color:#fff"><use href="#trophy"/></svg> Select League</span></div>
  <div class="col-head col-strong">
    <span style="left:19px;top:26px">Time</span><span style="left:109px;top:25px">Event</span>
    <span style="left:389px;top:9px">Full Time</span><span style="left:604px;top:9px">First Half</span>
    <span style="left:304px;top:41px">A 1x2</span><span style="left:375px;top:41px">HDP</span><span style="left:448px;top:41px">OV</span><span style="left:495px;top:41px">1x2</span>
    <span style="left:559px;top:41px">HDP</span><span style="left:625px;top:41px">OV</span><span style="left:686px;top:41px">1x2</span>
    <span style="left:744px;top:24px">+ More</span>
    <i class="vl" style="left:75px"></i><i class="vl" style="left:294px"></i><i class="vl" style="left:534px"></i><i class="vl" style="left:734px"></i>
    <i class="hl" style="left:294px;width:440px"></i>
  </div>
  <div class="league"><span class="star">★</span><span class="n">Coastal Premier League</span><svg class="r" width="20" height="20" style="color:#fff"><use href="#refresh"/></svg></div>
  <div class="row ra">
    <svg class="bars" width="14" height="12" style="fill:#666"><use href="#bars"/></svg><span style="left:38px;top:15px;color:#555">16:30</span><span style="left:38px;top:30px;color:var(--odd-red)">Live</span>
    <span style="left:84px;top:11px">★</span><span style="left:109px;top:11px">Bayside Mariners</span><span style="left:109px;top:29px;color:var(--odd-red)">Southgate Rovers</span>
    <span style="left:372px;top:9px">0.77</span><span class="ob" style="left:413px;top:9px">6-6.5</span><span class="or" style="left:455px;top:9px">o</span><span class="or" style="left:495px;top:9px">-0.85</span>
    <span class="ob" style="left:324px;top:30px">0-0.5</span><span class="or" style="left:369px;top:28px">-0.95</span><span class="or" style="left:455px;top:28px">u</span><span style="left:498px;top:28px">0.65</span>
    <span style="left:759px;top:22px">⇕ 13</span>
    <i class="div" style="left:29px"></i><i class="div" style="left:75px"></i><i class="div" style="left:294px"></i><i class="div" style="left:534px"></i>
  </div>
</div>

<div class="abs" style="left:293px;top:421px;width:794px">
  <div class="sec-head"><span class="t"><svg class="ic" width="20" height="20" style="color:#fff;margin-right:4px"><use href="#runner"/></svg> Today Non-Live</span><span class="c"><svg class="ic" width="14" height="14" style="color:#fff"><use href="#refresh"/></svg> 38</span><span class="s"><svg class="ic" width="16" height="16" style="color:#fff"><use href="#trophy"/></svg> Select League</span></div>
  <div class="col-head col-light">
    <span style="left:19px;top:26px">Time</span><span style="left:109px;top:25px">Event</span>
    <span style="left:389px;top:9px">Full Time</span><span style="left:604px;top:9px">First Half</span>
    <span style="left:304px;top:41px">A 1x2</span><span style="left:375px;top:41px">HDP</span><span style="left:448px;top:41px">OV</span><span style="left:495px;top:41px">1x2</span>
    <span style="left:559px;top:41px">HDP</span><span style="left:625px;top:41px">OV</span><span style="left:686px;top:41px">1x2</span>
    <span style="left:744px;top:24px">+ More</span>
    <i class="vl" style="left:75px"></i><i class="vl" style="left:294px"></i><i class="vl" style="left:534px"></i><i class="vl" style="left:734px"></i>
    <i class="hl" style="left:294px;width:440px"></i>
  </div>

  <div class="league"><span class="star">★</span><span class="n">Coastal Premier League</span><svg class="r" width="20" height="20" style="color:#fff"><use href="#refresh"/></svg></div>
  <div class="row rg">
    <svg class="bars" width="14" height="12" style="fill:#666"><use href="#bars"/></svg><span style="left:38px;top:15px;color:#555">16:30</span><span style="left:38px;top:30px;color:var(--odd-red)">Live</span>
    <span style="left:84px;top:11px">★</span><span style="left:109px;top:11px">Bayside Mariners</span><span style="left:109px;top:29px;color:var(--odd-red)">Southgate Rovers</span>
    <span style="left:372px;top:9px">0.77</span><span class="ob" style="left:413px;top:9px">6-6.5</span><span class="or" style="left:455px;top:9px">o</span><span class="or" style="left:495px;top:9px">-0.85</span>
    <span class="ob" style="left:324px;top:30px">0-0.5</span><span class="or" style="left:369px;top:28px">-0.95</span><span class="or" style="left:455px;top:28px">u</span><span style="left:498px;top:28px">0.65</span>
    <span style="left:759px;top:22px">⇕ 13</span>
    <i class="div" style="left:29px"></i><i class="div" style="left:75px"></i><i class="div" style="left:294px"></i><i class="div" style="left:534px"></i>
  </div>

  <div class="league"><span class="star">★</span><span class="n">Coastal Premier League</span><svg class="r" width="20" height="20" style="color:#fff"><use href="#refresh"/></svg></div>
  <div class="row rb">
    <svg class="bars" width="14" height="12" style="fill:#666"><use href="#bars"/></svg><span style="left:38px;top:15px;color:#555">16:30</span><span style="left:38px;top:30px;color:var(--odd-red)">Live</span>
    <span style="left:84px;top:11px">★</span><span style="left:109px;top:11px">Bayside Mariners</span><span style="left:109px;top:29px;color:var(--odd-red)">Southgate Rovers</span>
    <span style="left:372px;top:9px">0.77</span><span class="ob" style="left:413px;top:9px">6-6.5</span><span class="or" style="left:455px;top:9px">o</span><span class="or" style="left:495px;top:9px">-0.85</span>
    <span class="ob" style="left:324px;top:30px">0-0.5</span><span class="or" style="left:369px;top:28px">-0.95</span><span class="or" style="left:455px;top:28px">u</span><span style="left:498px;top:28px">0.65</span>
    <span style="left:759px;top:22px">⇕ 13</span>
    <i class="div" style="left:29px"></i><i class="div" style="left:75px"></i><i class="div" style="left:294px"></i><i class="div" style="left:534px"></i>
  </div>
  <div class="row rg">
    <svg class="bars" width="14" height="12" style="fill:#666"><use href="#bars"/></svg><span style="left:38px;top:15px;color:#555">16:30</span><span style="left:38px;top:30px;color:var(--odd-red)">Live</span>
    <span style="left:84px;top:11px">★</span><span style="left:109px;top:11px">Bayside Mariners</span><span style="left:109px;top:29px;color:var(--odd-red)">Southgate Rovers</span>
    <span style="left:372px;top:9px">0.77</span><span class="ob" style="left:413px;top:9px">6-6.5</span><span class="or" style="left:455px;top:9px">o</span><span class="or" style="left:495px;top:9px">-0.85</span>
    <span class="ob" style="left:324px;top:30px">0-0.5</span><span class="or" style="left:369px;top:28px">-0.95</span><span class="or" style="left:455px;top:28px">u</span><span style="left:498px;top:28px">0.65</span>
    <span style="left:759px;top:22px">⇕ 13</span>
    <i class="div" style="left:29px"></i><i class="div" style="left:75px"></i><i class="div" style="left:294px"></i><i class="div" style="left:534px"></i>
  </div>

  <div class="league"><span class="star">★</span><span class="n">Coastal Premier League</span><svg class="r" width="20" height="20" style="color:#fff"><use href="#refresh"/></svg></div>
  <div class="row rw">
    <svg class="bars" width="14" height="12" style="fill:#666"><use href="#bars"/></svg><span style="left:38px;top:15px;color:#555">16:30</span><span style="left:38px;top:30px;color:var(--odd-red)">Live</span>
    <span style="left:84px;top:11px">★</span><span style="left:109px;top:11px">Bayside Mariners</span><span style="left:109px;top:29px;color:var(--odd-red)">Southgate Rovers</span>
    <span style="left:372px;top:9px">0.77</span><span class="ob" style="left:413px;top:9px">6-6.5</span><span class="or" style="left:455px;top:9px">o</span><span class="or" style="left:495px;top:9px">-0.85</span>
    <span class="ob" style="left:324px;top:30px">0-0.5</span><span class="or" style="left:369px;top:28px">-0.95</span><span class="or" style="left:455px;top:28px">u</span><span style="left:498px;top:28px">0.65</span>
    <span style="left:759px;top:22px">⇕ 13</span>
    <i class="div" style="left:29px"></i><i class="div" style="left:75px"></i><i class="div" style="left:294px"></i><i class="div" style="left:534px"></i>
  </div>
  <div class="row rg">
    <svg class="bars" width="14" height="12" style="fill:#666"><use href="#bars"/></svg><span style="left:38px;top:15px;color:#555">16:30</span><span style="left:38px;top:30px;color:var(--odd-red)">Live</span>
    <span style="left:84px;top:11px">★</span><span style="left:109px;top:11px">Bayside Mariners</span><span style="left:109px;top:29px;color:var(--odd-red)">Southgate Rovers</span>
    <span style="left:372px;top:9px">0.77</span><span class="ob" style="left:413px;top:9px">6-6.5</span><span class="or" style="left:455px;top:9px">o</span><span class="or" style="left:495px;top:9px">-0.85</span>
    <span class="ob" style="left:324px;top:30px">0-0.5</span><span class="or" style="left:369px;top:28px">-0.95</span><span class="or" style="left:455px;top:28px">u</span><span style="left:498px;top:28px">0.65</span>
    <span style="left:759px;top:22px">⇕ 13</span>
    <i class="div" style="left:29px"></i><i class="div" style="left:75px"></i><i class="div" style="left:294px"></i><i class="div" style="left:534px"></i>
  </div>
  <div class="row rw">
    <svg class="bars" width="14" height="12" style="fill:#666"><use href="#bars"/></svg><span style="left:38px;top:15px;color:#555">16:30</span><span style="left:38px;top:30px;color:var(--odd-red)">Live</span>
    <span style="left:84px;top:11px">★</span><span style="left:109px;top:11px">Bayside Mariners</span><span style="left:109px;top:29px;color:var(--odd-red)">Southgate Rovers</span>
    <span style="left:372px;top:9px">0.77</span><span class="ob" style="left:413px;top:9px">6-6.5</span><span class="or" style="left:455px;top:9px">o</span><span class="or" style="left:495px;top:9px">-0.85</span>
    <span class="ob" style="left:324px;top:30px">0-0.5</span><span class="or" style="left:369px;top:28px">-0.95</span><span class="or" style="left:455px;top:28px">u</span><span style="left:498px;top:28px">0.65</span>
    <span style="left:759px;top:22px">⇕ 13</span>
    <i class="div" style="left:29px"></i><i class="div" style="left:75px"></i><i class="div" style="left:294px"></i><i class="div" style="left:534px"></i>
  </div>
  <div class="row rg">
    <svg class="bars" width="14" height="12" style="fill:#666"><use href="#bars"/></svg><span style="left:38px;top:15px;color:#555">16:30</span><span style="left:38px;top:30px;color:var(--odd-red)">Live</span>
    <span style="left:84px;top:11px">★</span><span style="left:109px;top:11px">Bayside Mariners</span><span style="left:109px;top:29px;color:var(--odd-red)">Southgate Rovers</span>
    <span style="left:372px;top:9px">0.77</span><span class="ob" style="left:413px;top:9px">6-6.5</span><span class="or" style="left:455px;top:9px">o</span><span class="or" style="left:495px;top:9px">-0.85</span>
    <span class="ob" style="left:324px;top:30px">0-0.5</span><span class="or" style="left:369px;top:28px">-0.95</span><span class="or" style="left:455px;top:28px">u</span><span style="left:498px;top:28px">0.65</span>
    <span style="left:759px;top:22px">⇕ 13</span>
    <i class="div" style="left:29px"></i><i class="div" style="left:75px"></i><i class="div" style="left:294px"></i><i class="div" style="left:534px"></i>
  </div>
  <div class="row rb">
    <svg class="bars" width="14" height="12" style="fill:#666"><use href="#bars"/></svg><span style="left:38px;top:15px;color:#555">16:30</span><span style="left:38px;top:30px;color:var(--odd-red)">Live</span>
    <span style="left:84px;top:11px">★</span><span style="left:109px;top:11px">Bayside Mariners</span><span style="left:109px;top:29px;color:var(--odd-red)">Southgate Rovers</span>
    <span style="left:372px;top:9px">0.77</span><span class="ob" style="left:413px;top:9px">6-6.5</span><span class="or" style="left:455px;top:9px">o</span><span class="or" style="left:495px;top:9px">-0.85</span>
    <span class="ob" style="left:324px;top:30px">0-0.5</span><span class="or" style="left:369px;top:28px">-0.95</span><span class="or" style="left:455px;top:28px">u</span><span style="left:498px;top:28px">0.65</span>
    <span style="left:759px;top:22px">⇕ 13</span>
    <i class="div" style="left:29px"></i><i class="div" style="left:75px"></i><i class="div" style="left:294px"></i><i class="div" style="left:534px"></i>
  </div>
  <div class="row rg">
    <svg class="bars" width="14" height="12" style="fill:#666"><use href="#bars"/></svg><span style="left:38px;top:15px;color:#555">16:30</span><span style="left:38px;top:30px;color:var(--odd-red)">Live</span>
    <span style="left:84px;top:11px">★</span><span style="left:109px;top:11px">Bayside Mariners</span><span style="left:109px;top:29px;color:var(--odd-red)">Southgate Rovers</span>
    <span style="left:372px;top:9px">0.77</span><span class="ob" style="left:413px;top:9px">6-6.5</span><span class="or" style="left:455px;top:9px">o</span><span class="or" style="left:495px;top:9px">-0.85</span>
    <span class="ob" style="left:324px;top:30px">0-0.5</span><span class="or" style="left:369px;top:28px">-0.95</span><span class="or" style="left:455px;top:28px">u</span><span style="left:498px;top:28px">0.65</span>
    <span style="left:759px;top:22px">⇕ 13</span>
    <i class="div" style="left:29px"></i><i class="div" style="left:75px"></i><i class="div" style="left:294px"></i><i class="div" style="left:534px"></i>
  </div>
</div>

<div class="abs footer">
  <div style="margin-top:26px">Betting Rules &nbsp; | &nbsp; Contact us &nbsp; | &nbsp; Privacy Policy &nbsp; | &nbsp; Responsible Gambling &nbsp; | &nbsp; Terms &amp; Conditions &nbsp; | &nbsp; Tutorials</div>
  <div style="margin-top:12px">Copyright © 2014 Name. &nbsp; All rights reserved.</div>
</div>

</div>
</body>
</html>
```